Creative flyer for small business IT services

We are an IT services company based in Western Australia. We're looking to expand our market share amongst small businesses and need a brochure/flyer designed to give them a good overview of why we can help them. The design and layout should be consistent with an existing company profile brochure (included) but please be creative. A comprehensive brief with copy and a rough layout is included.

Small Business

```html
<!DOCTYPE html>
<html lang="en">
<head>
<meta charset="utf-8">
<title>Small Business IT Solutions – Northgrid</title>
<link rel="stylesheet" href="https://fonts.googleapis.com/css2?family=Fira+Sans:wght@700;800&family=Open+Sans:wght@300;400;600;700&display=swap">
<style>
  :root {
    --brand-red: #a51d24;
    --ink: #2b2b2b;
    --body: #3c3c3c;
    --panel: #e6e6e8;
    --rule: #9a9a9a;
    --page: #ffffff;
    --stage: #474747;
  }
  * { box-sizing: border-box; margin: 0; padding: 0; }
  html, body { width: 881px; height: 1200px; overflow: hidden; }
  body { background: var(--stage); font-family: "Open Sans", Arial, sans-serif; color: var(--body); }
  .flyer { position: absolute; left: 56px; top: 56px; width: 770px; height: 1089px; background: var(--page); }
  .abs { position: absolute; }

  .masthead { left: 0; top: 0; width: 770px; height: 180px; background: var(--brand-red); }
  .masthead__title { left: 38px; top: 108px; color: #fff; font-size: 31px; font-weight: 400; letter-spacing: -0.2px; }
  .brand-tile { left: 644px; top: 27px; width: 98px; height: 92px; background: #fff; }
  .brand-tile__name { left: 644px; top: 128px; width: 98px; text-align: center; color: #fff; font-size: 15px; font-weight: 400; }

  .hero__headline { left: 38px; top: 210px; z-index: 2; font-family: "Fira Sans", Arial, sans-serif; font-weight: 800; font-size: 23px; color: var(--ink); }
  .hero__sub { left: 38px; top: 238px; z-index: 2; font-size: 23px; font-weight: 300; color: var(--ink); }
  .hero__image { left: 24px; top: 278px; width: 740px; height: 90px;
    background: linear-gradient(180deg, #ffffff 0%, #e6f0d8 30%, #a4c972 55%, #7a4a2c 80%, #5b341d 100%); }
  .hero__band { left: 0; top: 387px; width: 770px; height: 13px; background: var(--brand-red); }

  .intro__title { left: 46px; top: 434px; font-size: 21px; font-weight: 300; color: var(--ink); }
  .intro__text { left: 46px; top: 472px; width: 490px; font-size: 13px; line-height: 19px; letter-spacing: -0.1px; }
  .reasons__title { left: 58px; top: 551px; font-size: 13.4px; font-weight: 700; color: var(--brand-red); }
  .reason { font-size: 12.2px; line-height: 16px; width: 200px; padding-left: 19px; }
  .reason svg { position: absolute; left: 0; top: 2px; }

  .service { left: 38px; width: 487px; background: var(--panel); }
  .service__label { position: absolute; left: 0; width: 94px; top: 10px; text-align: center; font-size: 11px; font-weight: 700; line-height: 13px; color: var(--ink); }
  .service__icon { position: absolute; left: 26px; }
  .service__rule { position: absolute; left: 94px; width: 1px; background: var(--rule); }
  .service__copy { position: absolute; left: 106px; width: 378px; font-size: 9.1px; line-height: 12.6px; letter-spacing: -0.05px; color: #333; }
  .service__copy p + p { margin-top: 3px; }

  .sidebar { left: 548px; top: 425px; width: 183px; height: 557px; border: 1px solid #a8a8a8; border-right: none; }
  .sidebar__edge { left: 709px; top: 425px; }
  .sidebar__inner { left: 561px; top: 441px; width: 166px; font-size: 9.9px; line-height: 14.2px; letter-spacing: -0.1px; color: #444; }
  .sidebar h3 { font-size: 10.6px; font-weight: 700; color: var(--brand-red); margin-bottom: 1px; }
  .sidebar p { margin-bottom: 14px; }
  .sidebar .cite { text-align: right; margin-top: -14px; margin-bottom: 14px; }
  .sidebar .cite b { display: block; color: var(--ink); }

  .footer__mark { left: 40px; top: 1011px; width: 30px; height: 30px; background: var(--brand-red); }
  .footer__name { left: 78px; top: 1013px; font-size: 17px; font-weight: 400; color: var(--ink); }
  .footer__rule { top: 1004px; width: 1px; height: 42px; background: var(--brand-red); }
  .footer__info { top: 1015px; font-size: 9.4px; line-height: 12px; text-align: center; color: #333; }
  .footer__phone { left: 610px; top: 1017px; font-size: 16px; font-weight: 700; color: var(--ink); }
  .footer__band { left: 0; top: 1062px; width: 770px; height: 27px; background: var(--brand-red); }
</style>
</head>
<body>
<main class="flyer">
  <header class="abs masthead"></header>
  <h1 class="abs masthead__title">Small Business IT Solutions</h1>
  <div class="abs brand-tile"></div>
  <div class="abs brand-tile__name">northgrid</div>

  <div class="abs hero__image" role="img" aria-label="Row of six seedlings in mounds of soil, growing taller from left to right"></div>
  <h2 class="abs hero__headline">Small business. Big ideas.</h2>
  <p class="abs hero__sub">We’ll help your business grow.</p>
  <div class="abs hero__band"></div>

  <h2 class="abs intro__title">We help small businesses get ahead of the pack.</h2>
  <p class="abs intro__text">You’ve always got more to do. In a small business, the last thing you need is another hat to wear. You shouldn’t need to become a computer engineer to keep your business running smoothly. Say goodbye to IT headaches - our mission is to make your life easier.</p>

  <h3 class="abs reasons__title">Here’s why small businesses love Northgrid:</h3>
  <div class="abs reason" style="left:36px;top:575px"><svg width="14" height="12" viewBox="0 0 14 12"><path d="M1 6 L5 10 L13 1" fill="none" stroke="#a51d24" stroke-width="2.6"/></svg>We’re small business IT experts</div>
  <div class="abs reason" style="left:36px;top:596px"><svg width="14" height="12" viewBox="0 0 14 12"><path d="M1 6 L5 10 L13 1" fill="none" stroke="#a51d24" stroke-width="2.6"/></svg>We speak plain English and won’t waste your time</div>
  <div class="abs reason" style="left:264px;top:577px;width:260px"><svg width="14" height="12" viewBox="0 0 14 12"><path d="M1 6 L5 10 L13 1" fill="none" stroke="#a51d24" stroke-width="2.6"/></svg>We care about our relationships</div>
  <div class="abs reason" style="left:264px;top:598px;width:260px"><svg width="14" height="12" viewBox="0 0 14 12"><path d="M1 6 L5 10 L13 1" fill="none" stroke="#a51d24" stroke-width="2.6"/></svg>We worry about IT so you don’t have to</div>

  <section class="abs service" style="top:650px;height:100px">
    <div class="service__label">SUPPORT<br>SERVICES</div>
    <svg class="service__icon" style="top:40px" width="44" height="46" viewBox="0 0 44 46" fill="#a51d24">
      <path d="M6 4 L12 2 L40 34 L36 40 Z"/><path d="M33 36 L42 44 L38 46 L31 39 Z"/>
      <path d="M34 3 a9 9 0 0 0 -9 12 L5 35 a3.5 3.5 0 0 0 5 5 L30 20 a9 9 0 0 0 12 -9 l-5 4 l-4 -1 l-1 -4 l4 -5 a9 9 0 0 0 -2 -2 z"/>
    </svg>
    <div class="service__rule" style="top:12px;height:76px"></div>
    <div class="service__copy" style="top:9px">
      <p>Say goodbye to IT interruptions, slow services, confusing jargon and inexplicable errors. We have solutions to your IT problems, and packages to suit every budget. We can even come to your workplace. If you run into a problem or need something done, just contact our Service Desk.</p>
      <p>Whether you have a single computer or a big team with complex requirements, our expert team can assist. We’ll give you an entire IT department for a fraction of the cost.</p>
    </div>
  </section>

  <section class="abs service" style="top:764px;height:112px">
    <div class="service__label">MONITORING<br>&amp; BACKUP</div>
    <svg class="service__icon" style="top:40px" width="52" height="62" viewBox="0 0 52 62" fill="#a51d24">
      <rect x="0" y="0" width="36" height="12" rx="2"/><rect x="0" y="15" width="36" height="12" rx="2"/><rect x="0" y="30" width="24" height="12" rx="2"/><rect x="0" y="45" width="20" height="12" rx="2"/>
      <circle cx="33" cy="42" r="11" fill="none" stroke="#a51d24" stroke-width="4"/><path d="M40 50 L49 60 L52 57 L43 47 Z"/>
    </svg>
    <div class="service__rule" style="top:10px;height:92px"></div>
    <div class="service__copy" style="top:9px">
      <p>Most of us insure our cars and homes, yet small businesses often don’t protect themselves from the kind of disaster that strikes every day. Could your business recover from the complete loss of every electronic file - financial records, legal documents, customer information, intellectual property, archives, emails and more?</p>
      <p>Our Monitor &amp; Protect solutions keep you safe from physical threats like theft, fire and floods, but also from electronic threats like viruses and hackers. Best of all - it happens automatically, so you can relax.</p>
    </div>
  </section>

  <section class="abs service" style="top:888px;height:66px">
    <div class="service__label">HARDWARE<br>&amp; SOFTWARE</div>
    <svg class="service__icon" style="top:36px" width="44" height="30" viewBox="0 0 44 30" fill="#a51d24">
      <rect x="0" y="0" width="44" height="24" rx="2"/><rect x="4" y="3" width="36" height="17" fill="#fff"/>
      <rect x="17" y="24" width="10" height="4"/><rect x="12" y="27" width="20" height="3"/>
      <circle cx="18" cy="12" r="5"/><circle cx="18" cy="12" r="2" fill="#fff"/><circle cx="28" cy="8" r="3.4"/><circle cx="28" cy="8" r="1.3" fill="#fff"/>
    </svg>
    <div class="service__rule" style="top:10px;height:50px"></div>
    <div class="service__copy" style="top:9px">
      <p>Every business needs the right tools for the job. We supply world class hardware and software products from all the leading global vendors and many more. Our strong partnerships and buying power mean we can save you money.</p>
      <p>From a single keyboard to an entire infrastructure, we always take the time to help you select the right products.</p>
    </div>
  </section>

  <div class="abs sidebar"></div>
  <svg class="abs sidebar__edge" width="24" height="560" viewBox="0 0 24 560">
    <path d="M22 0 V190 L4 204 L22 218 V557 H0" fill="#fff" stroke="#a8a8a8" stroke-width="1"/>
  </svg>
  <aside class="abs sidebar sidebar__inner" style="border:none;height:auto">
    <h3>AUDIT</h3>
    <p>It helps to know where you stand.</p>
    <p>Get a clearer picture of your IT systems with our obligation-free IT audit and consultation.</p>
    <p>Contact us today and we’ll provide you with expert insights into how your business can benefit from today’s amazing technology.</p>
    <h3 style="margin-top:18px">TESTIMONIALS</h3>
    <p>Don’t just take our word for it! Here’s what some satisfied customers have to say about Northgrid:</p>
    <p>“We are pleased to have Northgrid as part of our team. I recommend Northgrid for any business seeking a trustworthy, reliable and effective IT service provider.”</p>
    <p class="cite"><b>Leah Morton,</b>Coastline Imaging</p>
    <p>“Northgrid’s expertise has allowed us to test, analyse and improve the reliability and performance of our application, further improving the health and financial status of our business.”</p>
    <p class="cite"><b>Owen Hartley,</b>Ledgerline Pty Ltd</p>
  </aside>

  <footer>
    <div class="abs footer__mark"></div>
    <div class="abs footer__name">northgrid</div>
    <div class="abs footer__rule" style="left:196px"></div>
    <div class="abs footer__info" style="left:206px;width:176px">Level 12, 80 Harbour Terrace<br>Perth WA 6000</div>
    <div class="abs footer__rule" style="left:384px"></div>
    <div class="abs footer__info" style="left:392px;width:178px">sales@northgrid.com.au<br><b>www.northgrid.com.au</b></div>
    <div class="abs footer__rule" style="left:571px"></div>
    <div class="abs footer__phone">1300 555 019</div>
    <div class="abs footer__band"></div>
  </footer>
</main>
</body>
</html>
```